Borealis Pictures are looking for a poster design for a new short film called "Paper Lanterns"
The film will be submitted to all major film festivals so great exposure....

Paper Lanterns was written and directed by Leo Brantley. Produced by Borealis Pictures. Starring Ray Cobden, Hannah Pryce, Tom Brantley, Neil Fairbrook and Gavin Ross.

Synopsis: Paper Lanterns, tells the story of Vic. A want-away agent/hit man for an undisclosed body, who is sent on a mysterious mission for his final assignment.
Whilst waiting on his last instructions in a hideaway, he meets Olena and Hugh and begins to snatch at the real life he's craved for so long.
In danger of taking his eye off the ball too soon, Vic must kill time and fight loneliness, for just one more day.

To give you an feel for the film here is the trailer on Youtube http://www.clipvault-example.com/watch?v=qL7mZt2PxRa.

Please can you put borealis website www.borealispictures-example.co.uk on the design.

Best of luck

```html
<!DOCTYPE html>
<html lang="en">
<head>
<meta charset="utf-8">
<title>Paper Lanterns – Poster</title>
<link rel="stylesheet" href="https://fonts.googleapis.com/css2?family=Poiret+One&family=Arimo:wght@400;700&display=swap">
<style>
  :root {
    --stage: #0d1413;
    --poster-black: #141112;
    --blood-red: #e21f26;
    --blood-dark: #a8141a;
    --cocoa: #3b2522;
    --accent-red: #e1262b;
    --white: #ffffff;
    --photo-dark: #1c1716;
    --photo-mid: #3a302b;
    --photo-skin: #6e5547;
    --note-yellow: #d8d64a;
  }
  * { margin: 0; padding: 0; box-sizing: border-box; }
  html, body { width: 1200px; height: 1200px; overflow: hidden; background: var(--stage); }
  .canvas { position: relative; width: 1200px; height: 1200px; }

  .poster {
    position: absolute; left: 177px; top: 19px;
    width: 845px; height: 1162px;
    background: var(--poster-black);
    border: 3px solid var(--white);
    overflow: hidden;
  }
  .poster > * { position: absolute; }

  .title-word {
    font-family: "Poiret One", sans-serif;
    font-weight: 400;
    color: var(--white);
    line-height: 1;
    white-space: nowrap;
  }

  .splash-block {
    left: 0; top: 0; width: 358px; height: 433px;
    background: radial-gradient(circle at 40% 45%, var(--blood-red) 0%, #d01a21 55%, var(--blood-dark) 100%);
  }
  .title-first { left: 40px; top: 238px; font-size: 110px; }

  .divider-vertical { left: 426px; top: 176px; width: 4px; height: 380px; background: var(--white); }
  .divider-horizontal { left: 161px; top: 553px; width: 269px; height: 5px; background: var(--accent-red); }

  .cocoa-block { left: 496px; top: 176px; width: 346px; height: 383px; background: var(--cocoa); }
  .title-second { left: 520px; top: 338px; font-size: 82px; }

  .hero-still {
    left: 0; top: 560px; width: 100%; height: 387px;
    background:
      radial-gradient(ellipse 180px 200px at 66% 30%, var(--photo-skin) 0%, rgba(110,85,71,0.35) 45%, rgba(0,0,0,0) 75%),
      radial-gradient(ellipse 140px 180px at 28% 45%, rgba(120,100,85,0.45) 0%, rgba(0,0,0,0) 70%),
      radial-gradient(ellipse at 60% 50%, var(--photo-mid) 0%, var(--photo-dark) 60%, var(--poster-black) 100%);
  }

  .credits {
    left: 46px; top: 722px;
    font-family: "Arimo", sans-serif; color: var(--white);
    font-size: 20px; line-height: 1.3;
    white-space: nowrap;
  }
  .credits dt { font-weight: 700; }
  .credits dd { font-weight: 400; margin-bottom: 20px; }
  .credits dd:last-child { margin-bottom: 0; }

  .stills-strip {
    left: 0; top: 947px; width: 100%; height: 150px;
    background: var(--accent-red);
    padding: 8px 0;
    display: flex; gap: 9px;
  }
  .still { flex: 1; height: 100%; }
  .still-figure {
    background:
      radial-gradient(ellipse 70px 90px at 48% 35%, #0e0b0a 0%, rgba(14,11,10,0.6) 60%, rgba(0,0,0,0) 100%),
      linear-gradient(90deg, #2a2320, #6a5646 55%, #3a2e26);
  }
  .still-note {
    background:
      radial-gradient(ellipse 55px 50px at 58% 48%, var(--note-yellow) 0%, #b5ad48 55%, rgba(0,0,0,0) 100%),
      linear-gradient(135deg, #5a4a3a, #7a6a4a 50%, #4a3c30);
  }
  .still-woman {
    background:
      radial-gradient(ellipse 60px 70px at 62% 45%, #c9a694 0%, rgba(140,105,90,0.5) 55%, rgba(0,0,0,0) 100%),
      linear-gradient(135deg, #e0dcd8, #a8968c 55%, #3a2a25);
  }

  .footer-bar {
    left: 0; top: 1097px; width: 100%; height: 62px;
    background: linear-gradient(to bottom, #2a2627, #050505);
    display: flex; align-items: center; justify-content: center;
    font-family: "Arimo", sans-serif; font-size: 20px; color: var(--white);
  }
</style>
</head>
<body>
<main class="canvas">
  <article class="poster">
    <div class="splash-block" role="img" aria-label="Red paint splatter texture"></div>
    <h1 class="title-word title-first">Paper</h1>

    <div class="divider-vertical"></div>
    <div class="divider-horizontal"></div>

    <div class="cocoa-block"></div>
    <span class="title-word title-second">Lanterns</span>

    <div class="hero-still" role="img" aria-label="Film still of a man in a dim room with a hand raised toward him"></div>

    <dl class="credits">
      <dt>Written and directed by</dt>
      <dd>Leo Brantley</dd>
      <dt>Produced by</dt>
      <dd>Borealis Pictures.</dd>
      <dt>Starring</dt>
      <dd>Ray Cobden, Hannah Pryce, Tom Brantley, Neil Fairbrook and Gavin Ross</dd>
    </dl>

    <section class="stills-strip">
      <div class="still still-figure" role="img" aria-label="Film still of a dark figure in a doorway"></div>
      <div class="still still-note" role="img" aria-label="Film still of a hand holding a yellow sticky note signed by Olena and Vic"></div>
      <div class="still still-woman" role="img" aria-label="Film still of a smiling woman in a bright room"></div>
    </section>

    <footer class="footer-bar">www.borealispictures-example.co.uk</footer>
  </article>
</main>
</body>
</html>
```